Professional Home Buyer business card needed

I need a pretty straight forward business card designed. We help people that NEED to sell their homes solve problems. We perform all types of Real Estate transactions including flip, wholesale, investment, rental property and multi family. The card will mainly be used to give to prospective Sellers but will also be given to Real Estate Investors as well. It should professional and very easy to read, most clients are older people.

Target Market(s)

Distressed home sellers as well as Real Estate investors

Industry/Entity Type

Real Estate

Contact Information for Business Card

should be a professional layout

Colors
ec1f27
ffffff
000000

Requirements
Must have
• Large logo on back and smaller one on front. should utilize Red, white, and black.
• I am thinking of using a soft touch coating on the card so keep that in mind.
• Contact info should be very easy to read, think older clients.
Nice to have
• I would like to see a design with rounded corners on the card
Should not have
• pictures of homes or other home graphics.

```html
<!DOCTYPE html>
<html lang="en">
<head>
<meta charset="utf-8">
<title>Crestline Home Buyers – Business Card</title>
<link rel="stylesheet" href="https://fonts.googleapis.com/css2?family=Michroma&family=Source+Sans+3:wght@400;700&display=swap">
<style>
  :root {
    --stage: #666666;
    --card-dark: #232324;
    --card-mid: #323233;
    --red: #ec1f27;
    --red-deep: #c4161c;
    --white: #ffffff;
    --black: #000000;
    --icon-bg: #e9e9e9;
  }
  * { box-sizing: border-box; margin: 0; padding: 0; }
  html, body {
    width: 1200px; height: 1200px; overflow: hidden;
    background: var(--stage);
  }
  .canvas { position: relative; width: 1200px; height: 1200px; }

  .card {
    position: absolute; left: 168px; width: 864px; height: 478px;
    border-radius: 32px;
    background: radial-gradient(ellipse at 45% 35%, var(--card-mid) 0%, var(--card-dark) 75%);
    overflow: hidden;
  }
  .card--front { top: 72px; }
  .card--back  { top: 602px; }

  .tagline {
    font-family: "Michroma", sans-serif; color: var(--white);
    white-space: nowrap; text-align: center;
  }
  .brand-name {
    font-family: "Source Sans 3", sans-serif; font-weight: 700;
    color: var(--white); text-align: center; line-height: 1;
    white-space: nowrap;
  }

  .card--front .logo-block {
    position: absolute; left: 0; width: 100%; top: 92px;
  }
  .card--front .tagline { font-size: 24px; letter-spacing: 0.4em; margin-bottom: 34px; }
  .card--front .brand-name__main { display: block; font-size: 120px; }
  .card--front .brand-name__sub  { display: block; font-size: 58px; margin-top: 22px; }

  .person { position: absolute; left: 56px; top: 38px; font-family: "Source Sans 3", sans-serif; }
  .person__name { font-size: 37px; color: var(--white); line-height: 1.1; }
  .person__role { font-size: 30px; color: var(--red); line-height: 1.2; margin-left: 4px; }

  .card--back .logo-block { position: absolute; left: 548px; width: 270px; top: 22px; }
  .card--back .tagline { font-size: 10px; letter-spacing: 0.3em; margin-bottom: 12px; }
  .card--back .brand-name__main { display: block; font-size: 50px; }
  .card--back .brand-name__sub  { display: block; font-size: 24px; margin-top: 8px; }

  .contact-list { position: absolute; left: 140px; top: 172px; list-style: none; }
  .contact-item {
    position: relative; width: 490px; height: 56px; margin-bottom: 17px;
    border-radius: 0 10px 10px 0;
    background: linear-gradient(90deg, var(--red) 0%, var(--red-deep) 100%);
    display: flex; align-items: center;
    font-family: "Source Sans 3", sans-serif; font-size: 26px; color: var(--white);
    padding-left: 28px;
  }
  .contact-icon {
    position: absolute; left: 427px; top: 13px; width: 30px; height: 30px;
    border-radius: 50%; background: var(--icon-bg);
    display: flex; align-items: center; justify-content: center;
  }
  .contact-icon svg { width: 16px; height: 16px; }
</style>
</head>
<body>
<main class="canvas">

  <section class="card card--front" aria-label="Card back side with large brand name">
    <div class="logo-block">
      <p class="tagline">SELL WITH CONFIDENCE</p>
      <p class="brand-name">
        <span class="brand-name__main">CRESTLINE</span>
        <span class="brand-name__sub">HOME BUYERS</span>
      </p>
    </div>
  </section>

  <section class="card card--back" aria-label="Card front side with contact details">
    <div class="person">
      <p class="person__name">Dana Whitfield</p>
      <p class="person__role">President</p>
    </div>

    <div class="logo-block">
      <p class="tagline">SELL WITH CONFIDENCE</p>
      <p class="brand-name">
        <span class="brand-name__main">CRESTLINE</span>
        <span class="brand-name__sub">HOME BUYERS</span>
      </p>
    </div>

    <ul class="contact-list">
      <li class="contact-item">316-555-0148
        <span class="contact-icon"><svg viewBox="0 0 16 16"><rect x="5" y="2" width="6" height="12" rx="1.5" fill="#333"/><rect x="6.3" y="4" width="3.4" height="4" fill="#eee"/></svg></span>
      </li>
      <li class="contact-item">dana@crestlinehomebuyers.com
        <span class="contact-icon"><svg viewBox="0 0 16 16"><rect x="2" y="4" width="12" height="8" fill="none" stroke="#333" stroke-width="1.4"/><path d="M2 4 L8 9 L14 4" fill="none" stroke="#333" stroke-width="1.4"/></svg></span>
      </li>
      <li class="contact-item">www.crestlinehomebuyers.com
        <span class="contact-icon"><svg viewBox="0 0 16 16"><circle cx="8" cy="8" r="5.5" fill="none" stroke="#333" stroke-width="1.4"/><path d="M2.5 8 H13.5 M8 2.5 V13.5" stroke="#333" stroke-width="1.2"/></svg></span>
      </li>
      <li class="contact-item">P.O. Box 12 Fairhaven, KS 67999
        <span class="contact-icon"><svg viewBox="0 0 16 16"><path d="M2.5 8 L8 3 L13.5 8" fill="none" stroke="#333" stroke-width="1.5"/><path d="M4.5 7.5 V13 H11.5 V7.5" fill="none" stroke="#333" stroke-width="1.5"/></svg></span>
      </li>
    </ul>
  </section>

</main>
</body>
</html>
```